Business Card and Letterhead for new HR Consultancy

A business card and letterhead design that includes the logo (attached in jpg) and the business tag line which is "Investing in Your Greatest Asset"
We are based in regional New South Wales, Australia and provide HR services to small and medium business owners to support them grow their businesses by focusing on their people. The services provided cover the full range of HR management from simple advice through to comprehensive programs that support people management. My clients typically will not have a HR manager, either because they don't need to employ one or can't afford to hire one. So they will be looking for me to provide good services, add value to their business for a competitive price.
I am a middle aged woman with over 15 years expertise in all facets of HR Management. My clients need to know they can trust me, that I am credible and competent and open in my relationship with them and that I can make a positive difference for them.
I would like to see designs that are modern and communicate value for money.
A note to advise that the email address is
xxxxxxx@wattlecrestteam.com.au
website will be
www.wattlecrestteam.com.au
thanks
L.
Will also need to include the business number (indicates it is a registered business).
ABN: 38 217 405 963
Target Market(s)
small to medium sized business owners 30 years and over, professional and tradespeople
Industry/Entity Type
Business
Look and feel

```html
<!DOCTYPE html>
<html lang="en">
<head>
<meta charset="utf-8">
<title>Wattlecrest – Letterhead and Business Card</title>
<link rel="stylesheet" href="https://fonts.googleapis.com/css2?family=Arimo:wght@700&family=Questrial&display=swap">
<style>
  :root {
    --backdrop: #080808;
    --paper: #ffffff;
    --brand-green: #1b8f2e;
    --footer-green: #17893a;
    --hill-yellow: #fdcf3c;
    --card-yellow: #f3ea12;
    --card-green: #22b14c;
    --card-tan: #d9b24c;
    --wave-dark: #1d4a3a;
    --wave-gold: #f7dc5a;
    --ink: #1a1a1a;
    --white: #ffffff;
  }
  * { margin: 0; padding: 0; box-sizing: border-box; }
  html, body { width: 1200px; height: 1021px; overflow: hidden; background: var(--backdrop); }
  .stationery { position: relative; width: 1200px; height: 1021px; }

  .letterhead {
    position: absolute; left: 69px; top: 31px; width: 689px; height: 922px;
    background: var(--paper); overflow: hidden;
  }
  .letterhead__brand {
    position: absolute; top: 52px; left: 0; width: 100%;
    display: flex; justify-content: center; align-items: center; gap: 14px;
  }
  .brand-dot { width: 26px; height: 26px; border-radius: 50%; background: var(--brand-green); }
  .brand-name {
    font-family: "Questrial", sans-serif; color: var(--brand-green);
    font-size: 50px; line-height: 1; letter-spacing: -0.5px;
  }
  .letterhead__art { position: absolute; left: 0; top: 0; width: 689px; height: 922px; }
  .letterhead__tagline {
    position: absolute; left: 0; bottom: 0; width: 100%; height: 57px;
    display: flex; align-items: center; justify-content: center;
    font-family: "Arimo", sans-serif; font-weight: 700; font-size: 24px; color: var(--white);
    padding-right: 20px;
  }

  .business-card {
    position: absolute; left: 552px; top: 297px; width: 572px; height: 328px; overflow: hidden;
  }
  .business-card__art { position: absolute; inset: 0; width: 572px; height: 328px; }
  .business-card__brand {
    position: absolute; left: 214px; top: 44px;
    display: flex; align-items: center; gap: 12px;
  }
  .business-card__brand .brand-dot { width: 22px; height: 22px; }
  .business-card__brand .brand-name { font-size: 44px; }
  .contact {
    position: absolute; left: 23px; top: 34px;
    font-family: "Questrial", sans-serif; color: var(--ink);
  }
  .contact__name, .contact__title { font-size: 23px; line-height: 29px; }
  .contact__details { margin-top: 8px; list-style: none; font-size: 19px; line-height: 24.5px; }
  .business-card__tagline {
    position: absolute; left: 52px; top: 249px;
    font-family: "Arimo", sans-serif; font-weight: 700; font-size: 23px; line-height: 30px;
    color: var(--white);
  }
</style>
</head>
<body>
<main class="stationery">

  <section class="letterhead" aria-label="Letterhead">
    <svg class="letterhead__art" viewBox="0 0 689 922" aria-hidden="true">
      <path d="M0 737 C 60 690 120 648 192 645 C 300 640 420 730 520 800 C 570 835 610 858 640 865 L 689 865 L 689 922 L 0 922 Z" fill="var(--hill-yellow)"/>
      <rect x="0" y="865" width="689" height="57" fill="var(--footer-green)"/>
    </svg>
    <div class="letterhead__brand">
      <span class="brand-dot"></span>
      <span class="brand-name">Wattlecrest</span>
    </div>
    <p class="letterhead__tagline">Investing in Your Greatest Asset</p>
  </section>

  <section class="business-card" aria-label="Business card">
    <svg class="business-card__art" viewBox="0 0 572 328" aria-hidden="true">
      <defs>
        <linearGradient id="card-sweep" x1="0" y1="0" x2="1" y2="0">
          <stop offset="0" stop-color="var(--card-yellow)"/>
          <stop offset="0.55" stop-color="var(--card-green)"/>
          <stop offset="1" stop-color="var(--card-tan)"/>
        </linearGradient>
      </defs>
      <rect width="572" height="328" fill="url(#card-sweep)"/>
      <ellipse cx="392" cy="64" rx="232" ry="116" fill="var(--card-green)"/>
      <ellipse cx="390" cy="52" rx="228" ry="114" fill="var(--paper)"/>
      <path d="M0 222 C 110 185 250 170 360 205 C 450 235 510 300 572 328 L 0 328 Z" fill="var(--wave-gold)"/>
      <path d="M0 236 C 110 200 250 188 350 220 C 430 248 480 300 520 328 L 0 328 Z" fill="var(--wave-dark)"/>
    </svg>
    <div class="business-card__brand">
      <span class="brand-dot"></span>
      <span class="brand-name">Wattlecrest</span>
    </div>
    <div class="contact">
      <p class="contact__name">Name</p>
      <p class="contact__title">Title</p>
      <ul class="contact__details">
        <li>Address</li>
        <li>Phone #</li>
        <li>e-mail</li>
        <li>Website</li>
      </ul>
    </div>
    <p class="business-card__tagline">Investing in Your<br>Greatest Asset</p>
  </section>

</main>
</body>
</html>
```